Honey Label for 1kg square jar

We require premium looking honey label for 1kg packed in dark amber jar as shown in the image.
Brand is called :"Brindova Honey" - logo to be provided
We would like the following colours to be considered (white, gold and red)
We like to have some flowers and beehives on the background.
The label covers 3 sides of the square jar and were hoping to see render of the front side which should include the brand and also the words" 100% Premium Australian Honey"

Need extra days to review

```html
<!DOCTYPE html>
<html lang="en">
<head>
<meta charset="utf-8">
<title>Brindova Honey – Wild Flower Honey Label</title>
<link rel="stylesheet" href="https://fonts.googleapis.com/css2?family=Josefin+Sans:wght@400;600&family=Great+Vibes&display=swap">
<style>
  :root {
    --backdrop: #3d080c;
    --label-white: #f8f6f1;
    --gold: #a8782c;
    --gold-soft: #d9c29a;
    --forest: #1d3a26;
    --ink-grey: #7a746b;
    --sketch-light: #efe6d6;
    --sketch-mid: #d8c4a2;
  }
  html, body {
    margin: 0;
    width: 1200px;
    height: 821px;
    overflow: hidden;
    background: var(--backdrop);
  }
  .canvas {
    position: relative;
    width: 1200px;
    height: 821px;
  }
  .label {
    position: absolute;
    left: 220px;
    top: 150px;
    width: 760px;
    height: 520px;
    background: var(--label-white);
    clip-path: polygon(6% 0, 94% 0, 100% 12%, 100% 88%, 94% 100%, 6% 100%, 0 88%, 0 12%);
    font-family: "Josefin Sans", sans-serif;
    color: var(--forest);
  }
  .label__rule {
    position: absolute;
    left: 0;
    right: 0;
    height: 3px;
    background: var(--gold);
  }
  .label__rule--top { top: 14px; }
  .label__rule--bottom { bottom: 14px; }
  .artwork {
    position: absolute;
    border-radius: 18px;
  }
  .artwork--honeycomb {
    left: 30px; top: 36px; width: 136px; height: 130px;
    background: radial-gradient(circle at 40% 40%, var(--sketch-mid), var(--sketch-light) 75%);
  }
  .artwork--jar-flowers {
    left: 40px; top: 300px; width: 200px; height: 170px;
    background: linear-gradient(135deg, var(--sketch-light), var(--sketch-mid));
  }
  .artwork--tree-hive {
    right: 36px; top: 150px; width: 136px; height: 320px;
    background: linear-gradient(180deg, var(--sketch-light), var(--sketch-mid));
  }
  .label__content {
    position: absolute;
    left: 180px;
    right: 180px;
    top: 50px;
    text-align: center;
  }
  .brand-name {
    margin: 0;
    font-size: 48px;
    font-weight: 600;
    color: var(--forest);
    line-height: 1.1;
    white-space: nowrap;
  }
  .claim {
    margin: 14px 0 0;
    font-size: 20px;
    letter-spacing: 2px;
  }
  .divider {
    width: 30px;
    height: 2px;
    margin: 10px auto 0;
    background: var(--gold);
  }
  .variety {
    margin: 14px 0 0;
    font-family: "Great Vibes", cursive;
    font-size: 44px;
    color: var(--gold);
    line-height: 1;
    white-space: nowrap;
  }
  .process {
    margin: 8px 0 0;
    font-size: 13px;
    letter-spacing: 3px;
    color: var(--ink-grey);
  }
  .weight-rule {
    width: 270px;
    height: 1px;
    margin: 16px auto 0;
    background: var(--gold);
  }
  .net-weight {
    margin: 14px 0 0;
    font-size: 19px;
    word-spacing: 4px;
  }
  .net-weight span {
    border-left: 1px solid var(--forest);
    padding-left: 8px;
    margin-left: 6px;
  }
  .premium-tag {
    display: inline-block;
    margin-top: 14px;
    padding: 6px 22px 4px;
    background: var(--forest);
    color: var(--gold-soft);
    font-size: 14px;
    letter-spacing: 1px;
  }
  .origin {
    margin: 12px 0 0;
    font-family: "Great Vibes", cursive;
    font-size: 30px;
    color: var(--forest);
  }
</style>
</head>
<body>
<main class="canvas">
  <section class="label">
    <div class="label__rule label__rule--top"></div>
    <div class="label__rule label__rule--bottom"></div>

    <div class="artwork artwork--honeycomb" role="img" aria-label="Engraved honeycomb with dripping honey"></div>
    <div class="artwork artwork--jar-flowers" role="img" aria-label="Engraved honey jar with wild flowers"></div>
    <div class="artwork artwork--tree-hive" role="img" aria-label="Engraved tree with a wooden beehive and flowers"></div>

    <div class="label__content">
      <h1 class="brand-name">Brindova Honey</h1>
      <p class="claim">100% NATURAL</p>
      <div class="divider"></div>
      <p class="variety">Wild Flower Honey</p>
      <p class="process">LIQUID NON PASTEURIZED</p>
      <div class="weight-rule"></div>
      <p class="net-weight">Net Wt.<span>1000g</span><span>1kg</span></p>
      <div class="premium-tag">100% PREMIUM</div>
      <p class="origin">Australian Honey</p>
    </div>
  </section>
</main>
</body>
</html>
```